Yard Sign Design for Roofing Contractor

We are looking for a new design for our yard signs used on all jobs we build. We are looking for a way to brand the company and are hoping that this contest can give us a "theme" we can incorporate into out other marketing items such as, vehicle graphics, apparel, etc... I have attached a copy of our logo to be used on the sign, it can be "shadowed" with a color to enhance the look and the sign, but please keep the basic logo design. Attached are some samples of construction colors the boss was thinking of along with a picture of our current yard sign to help give some direction and let you know what info is needed on the sign.The darker construction yellow may work better than the fluorescent yellow, but won't know without visual aid. We are not tied to any particular color as of now, so they do have freedom of design as long as keeping with the construction feel. (Just another thought, potentially a reflective construction tape look would be interesting so signs are visable at night)
Updates

Reason: Meeting with new web designers next week to discuss best option to incorporate into our website.Thank you for the submissions!

Target Market(s)

Want signs to stand out when driving by and visibility in neighborhood where sign is posted for potential referrals

Industry/Entity Type

Contractor

Colors
fbed22
fece3e
f37122

Requirements
Must have
• Information that is on our current signs, image attached. I uploaded a .pdf file showing some options that could work for adding "shading" to our logo if you choose to do so.
• Sign should measure 18" T, 24" W
Nice to have
• Interested is seeing designs using construction tape look, images attached

```html
<!DOCTYPE html>
<html lang="en">
<head>
<meta charset="utf-8">
<title>Kestrel Construction – Yard Sign</title>
<link rel="stylesheet" href="https://fonts.googleapis.com/css2?family=Cinzel:wght@900&family=Montserrat:wght@700;800&display=swap">
<style>
  :root {
    --sign-yellow: #fbd80f;
    --tape-yellow: #fece3e;
    --tape-black: #111111;
    --ink: #141414;
    --seal-orange: #f37122;
    --seal-fill: #fbbf3a;
    --badge-fill: #1c1c1c;
    --backdrop: #e9e9e6;
    --white: #ffffff;
  }
  * { margin: 0; padding: 0; box-sizing: border-box; }
  html, body {
    width: 1200px; height: 1000px; overflow: hidden;
    background: var(--backdrop);
  }
  .yard-sign {
    position: absolute; left: 40px; top: 80px;
    width: 1120px; height: 840px;
    background: var(--sign-yellow);
    overflow: hidden;
    box-shadow: 0 6px 20px rgba(0,0,0,.18);
  }
  .tape-band {
    position: absolute; left: 0; width: 100%; height: 92px;
    background: repeating-linear-gradient(-45deg,
      var(--tape-black) 0 34px, var(--tape-yellow) 34px 68px);
    border-top: 10px solid var(--tape-black);
    border-bottom: 10px solid var(--tape-black);
  }
  .tape-band--top { top: 0; }
  .tape-band--bottom { bottom: 0; }

  .award-seal {
    position: absolute; left: 52px; top: 140px;
    width: 150px; height: 150px; border-radius: 50%;
    background: var(--seal-fill);
    border: 9px solid var(--seal-orange);
    display: flex; align-items: center; justify-content: center;
    text-align: center;
    font-family: 'Montserrat', sans-serif; font-weight: 800;
    font-size: 24px; line-height: 1.2; color: var(--ink);
  }
  .accreditation-badge {
    position: absolute; right: 62px; top: 128px;
    width: 86px; height: 176px; border-radius: 6px;
    background: var(--badge-fill);
    border: 4px solid var(--white);
    outline: 2px solid var(--badge-fill);
  }

  .web-address {
    position: absolute; left: 0; right: 0; top: 226px;
    text-align: center;
    font-family: 'Montserrat', sans-serif; font-weight: 700;
    font-size: 40px; letter-spacing: .5px; color: var(--ink);
  }

  .brand-lockup {
    position: absolute; left: 0; right: 0; top: 300px;
    display: flex; align-items: center; justify-content: center;
    gap: 26px;
  }
  .brand-mark {
    width: 64px; height: 64px;
    background: var(--ink);
    flex: none;
  }
  .company-name {
    font-family: 'Cinzel', serif; font-weight: 900;
    color: var(--ink); line-height: .95; text-align: center;
  }
  .company-name__main { display: block; font-size: 150px; letter-spacing: 2px; }
  .company-name__sub { display: block; font-size: 74px; letter-spacing: 1px; }

  .service-list {
    position: absolute; left: 150px; right: 150px; top: 556px;
    display: flex; justify-content: space-between;
    list-style: none;
    font-family: 'Cinzel', serif; font-weight: 900;
    font-size: 44px; color: var(--ink);
  }
  .phone-number {
    position: absolute; left: 0; right: 0; top: 620px;
    text-align: center;
    font-family: 'Montserrat', sans-serif; font-weight: 800;
    font-size: 78px; line-height: 1.1; color: var(--ink); letter-spacing: 1px;
  }
</style>
</head>
<body>
  <main class="yard-sign">
    <div class="tape-band tape-band--top"></div>

    <div class="award-seal">Award<br>Winning</div>
    <div class="accreditation-badge" role="img" aria-label="Accreditation badge"></div>

    <p class="web-address">www.kestrelroofing.com</p>

    <header class="brand-lockup">
      <span class="brand-mark" aria-hidden="true"></span>
      <h1 class="company-name">
        <span class="company-name__main">KESTREL</span>
        <span class="company-name__sub">CONSTRUCTION</span>
      </h1>
    </header>

    <ul class="service-list">
      <li>ROOF</li>
      <li>SIDING</li>
      <li>GUTTERS</li>
    </ul>

    <p class="phone-number">636-555-0147</p>

    <div class="tape-band tape-band--bottom"></div>
  </main>
</body>
</html>
```